Option Sheet

We need a one page option sheet with a left to right reading of the five options. It should be a one sheet, multiple colors and definitive separations between options This is used in a sales consultation. Backround or colors not in option need to have the follow RGB value (5 red, 20 green, 63 blue)

We added a smaller text file, please change that point

Target Market(s)

Divorce

Industry/Entity Type

Legal

Requirements
Must have
• 1) All five options left to right
• 2)language included in sheet

```html
<!DOCTYPE html>
<html lang="en">
<head>
<meta charset="utf-8">
<title>Five Options – Divorce</title>
<link href="https://fonts.googleapis.com/css2?family=Montserrat:wght@400;800&family=Roboto:wght@700;900&family=Arimo:wght@400;700&display=swap" rel="stylesheet">
<style>
  :root {
    --sheet: rgb(5, 20, 63);
    --rule: #8fa3d6;
    --title: #5fb3ee;
    --subtitle: #ffffff;
    --blue: #0b64a3;
    --ink: #111111;
    --halo: #f8ec5c;
    --halo-soft: #fbf49a;
    --white: #ffffff;
  }
  * { box-sizing: border-box; margin: 0; padding: 0; }
  html, body { width: 948px; height: 1200px; overflow: hidden; background: var(--sheet); }
  .sheet {
    position: relative; width: 948px; height: 1200px; background: var(--sheet);
    font-family: "Arimo", Arial, sans-serif; color: var(--ink);
  }
  .frame {
    position: absolute; left: 30px; top: 30px; right: 30px; bottom: 30px;
    border: 1.5px solid var(--rule);
  }
  .title {
    position: absolute; top: 52px; left: 0; width: 100%; text-align: center;
    font-family: "Montserrat", sans-serif; font-weight: 400; font-size: 44px;
    letter-spacing: 7px; color: var(--title);
  }
  .subtitle {
    position: absolute; top: 110px; left: 0; width: 100%; text-align: center;
    font-family: "Montserrat", sans-serif; font-weight: 800; font-size: 30px;
    letter-spacing: 6px; color: var(--subtitle);
  }
  .option {
    position: absolute; border-radius: 50%; background: var(--white);
    box-shadow: 0 0 0 6px var(--halo-soft), 0 0 8px 9px var(--halo);
    display: flex; flex-direction: column; align-items: center; justify-content: center;
  }
  .option-number {
    font-family: "Roboto", sans-serif; font-weight: 900; font-size: 22px; color: var(--blue);
  }
  .option-name {
    font-family: "Roboto", sans-serif; font-weight: 700; font-size: 17px; color: var(--ink);
    margin-bottom: 6px;
  }
  .option-body { width: 78%; }
  .label { font-weight: 700; font-size: 14px; margin: 4px 0 2px; }
  .points { list-style: none; }
  .points li {
    font-size: 12.5px; line-height: 1.28; padding-left: 9px; margin: 2px 0 2px 2px; position: relative;
  }
  .points li::before {
    content: ""; position: absolute; left: 0; top: 6px; width: 4px; height: 4px;
    border-radius: 50%; background: var(--blue);
  }
  .opt-1 { left: 124px; top: 170px; width: 296px; height: 296px; }
  .opt-2 { left: 503px; top: 163px; width: 304px; height: 304px; }
  .opt-3 { left: 107px; top: 500px; width: 330px; height: 330px; }
  .opt-4 { left: 490px; top: 512px; width: 356px; height: 356px; }
  .opt-5 { left: 290px; top: 850px; width: 300px; height: 300px; }
  .opt-2 .option-body, .opt-4 .option-body { width: 80%; }
  .opt-4 .points li { font-size: 12px; }
</style>
</head>
<body>
<main class="sheet">
  <div class="frame"></div>
  <h1 class="title">FIVE OPTIONS</h1>
  <h2 class="subtitle">DIVORCE</h2>

  <section class="option opt-1">
    <h3 class="option-number">OPTION #1:</h3>
    <p class="option-name">Do Nothing</p>
    <div class="option-body">
      <p class="label">Advantages:</p>
      <ul class="points"><li>Stay married</li><li>No life Changes</li></ul>
      <p class="label">Disadvantages:</p>
      <ul class="points"><li>Remain unhappy, depressed, anxious</li><li>Money and assets may disappear</li><li>What is going to change?</li></ul>
    </div>
  </section>

  <section class="option opt-2">
    <h3 class="option-number">OPTION #2:</h3>
    <p class="option-name">Go to Counseling</p>
    <div class="option-body">
      <p class="label">Advantages:</p>
      <ul class="points"><li>Reconcile marriage</li><li>Help make a better life</li></ul>
      <p class="label">Disadvantages:</p>
      <ul class="points"><li>Past issues are highlighted and may drudge up old wounds</li><li>It may just clarify the reasons you need to separate and/or divorce</li><li>Both parties must be invested and willing to participate</li></ul>
    </div>
  </section>

  <section class="option opt-3">
    <h3 class="option-number">OPTION #3:</h3>
    <p class="option-name">Do it Yourself</p>
    <div class="option-body">
      <p class="label">Advantages:</p>
      <ul class="points"><li>No attorney fees</li><li>You are your on attorney</li></ul>
      <p class="label">Disadvantages:</p>
      <ul class="points"><li>People often find that what is “fair,” may in fact, not be truly fair</li><li>Often times, people do not know the risks</li><li>Complicated legal system within intrigue rules</li><li>Unsure how to complete the necessary paperwork and meet the deadlines</li></ul>
    </div>
  </section>

  <section class="option opt-4">
    <h3 class="option-number">OPTION #4:</h3>
    <p class="option-name">Limited Representation</p>
    <div class="option-body">
      <p class="label">Advantages:</p>
      <ul class="points"><li>Balance between going alone and our limited involvement in the case</li></ul>
      <p class="label">Disadvantages:</p>
      <ul class="points"><li>Our terms may not benefit from our legal knowledge</li><li>The legal consequences of your legal documents will not be explained to you so that you can formulate a plan for handling the rest of your case.</li><li>Your spouse or other parties may cause your legal fees to increase significantl without action on your part</li></ul>
    </div>
  </section>

  <section class="option opt-5">
    <h3 class="option-number">OPTION #5:</h3>
    <p class="option-name">Hire Us</p>
    <div class="option-body">
      <p class="label">Advantages:</p>
      <ul class="points"><li>Gain the full benefits of our experience</li><li>Have a team of Family Law focus attorneys</li><li>Often saves you or makes you money in the long run</li><li>Save you time, energy and stress</li></ul>
      <p class="label">Disadvantages:</p>
      <ul class="points"><li>Initial cost</li></ul>
    </div>
  </section>
</main>
</body>
</html>
```